Business card, invoice design and email signature for accounting firm
Tallyworks.Ca
Business card, invoice design and email signature for accounting firm - Financial Services
Creative Brief
Simple
Marta Elkins, BA, CGA
Certified General Accountant
47 Wexmoor Lane Brantwell, MB R4K2H5
marta@tallyworks.ca
www.tallyworks.ca
we don't need the letterhead and envelope.

```html
<!DOCTYPE html>
<html lang="en">
<head>
<meta charset="utf-8">
<title>Tallyworks.Ca – Business Card</title>
<link rel="stylesheet" href="https://fonts.googleapis.com/css2?family=Open+Sans:ital,wght@0,400;0,600;0,700;1,400&display=swap">
<style>
  :root {
    --backdrop: #e9eaec;
    --card: #ffffff;
    --purple: #5b2c8e;
    --purple-deep: #47206f;
    --green: #8cc63f;
    --green-light: #b5dc6b;
    --ink: #6d6e71;
    --white: #ffffff;
  }
  * { margin: 0; padding: 0; box-sizing: border-box; }
  html, body {
    width: 1200px; height: 838px; overflow: hidden;
    background: var(--backdrop);
    font-family: "Open Sans", Arial, sans-serif;
  }
  .canvas { position: relative; width: 1200px; height: 838px; }
  .card {
    position: absolute; width: 700px; height: 400px;
    background: var(--card); overflow: hidden;
    box-shadow: 0 12px 30px rgba(0,0,0,.18);
  }
  .card--back { left: 440px; top: 50px; }
  .card--front { left: 60px; top: 390px; }

  .brand {
    display: flex; align-items: center; gap: 12px;
    color: var(--purple); font-weight: 700; letter-spacing: .5px;
  }
  .brand__dot { width: 16px; height: 16px; border-radius: 50%; background: var(--green); }

  .card--back .brand {
    position: absolute; left: 0; right: 0; top: 165px;
    justify-content: center; font-size: 52px;
  }
  .card--back .brand__dot { width: 22px; height: 22px; }

  .card--front .brand { position: absolute; left: 56px; top: 46px; font-size: 40px; }

  .card__waves { position: absolute; left: 0; top: 0; width: 700px; height: 400px; }

  .holder { position: absolute; left: 56px; top: 128px; }
  .holder__name { color: var(--green); font-weight: 700; font-size: 24px; line-height: 1.2; }
  .holder__title { color: var(--ink); font-style: italic; font-size: 15px; margin-top: 2px; }
  .holder__address { color: var(--ink); font-size: 13px; line-height: 1.45; margin-top: 16px; }

  .contact {
    position: absolute; right: 34px; top: 262px;
    list-style: none; color: var(--white); font-size: 15px; text-align: right;
  }
  .contact li { display: flex; justify-content: flex-end; align-items: center; gap: 8px; line-height: 1.6; }
  .contact svg { width: 14px; height: 14px; fill: var(--white); }
</style>
</head>
<body>
<main class="canvas">

  <section class="card card--back" aria-label="Business card, back">
    <div class="brand"><span class="brand__dot"></span>Tallyworks.Ca</div>
  </section>

  <section class="card card--front" aria-label="Business card, front">
    <svg class="card__waves" viewBox="0 0 700 400" aria-hidden="true">
      <path d="M0 0 H150 C90 20 40 50 0 90 Z" fill="var(--purple)"/>
      <path d="M0 0 H180 C110 25 50 60 0 110 V90 C40 50 90 20 150 0 Z" fill="var(--green-light)"/>
      <path d="M0 300 C180 250 420 210 700 240 V400 H0 Z" fill="var(--green)"/>
      <path d="M0 315 C190 262 430 226 700 254 V400 H0 Z" fill="var(--purple)"/>
      <path d="M0 400 C200 370 450 360 700 330 V400 Z" fill="var(--purple-deep)" opacity=".5"/>
    </svg>

    <div class="brand"><span class="brand__dot"></span>Tallyworks.Ca</div>

    <div class="holder">
      <p class="holder__name">Marta Elkins, BA, CGA</p>
      <p class="holder__title">Certified General Accountant</p>
      <p class="holder__address">47 Wexmoor Lane<br>Brantwell, MB R4K2H5</p>
    </div>

    <ul class="contact">
      <li><svg viewBox="0 0 16 16"><path d="M3 1l3 3-2 2c1 2 3 4 5 5l2-2 3 3-2 2C6 14 2 10 1 3z"/></svg>555-014-7461</li>
      <li><svg viewBox="0 0 16 16"><path d="M4 0h8v16H4zM5.5 2v10h5V2zM7 13.5h2v1H7z" fill-rule="evenodd"/></svg>555-014-3918</li>
      <li><svg viewBox="0 0 16 16"><path d="M0 3h16v10H0zM1 4l7 5 7-5z" fill-rule="evenodd"/></svg>marta@tallyworks.ca</li>
      <li>www.tallyworks.ca</li>
    </ul>
  </section>

</main>
</body>
</html>
```